Brookfarrow Osteopathy and dry needling business card

Business card for Brookfarrow Osteopathy and Dry Needling.

Industry/Entity Type

Health

Contact Information for Business Card

I do not have a phone number yet. I also do not have an email address yet. The physical address is: 48 Lower Crane Street Brookfarrow The website is: www.brookfarrowosteosteopathy.example My details are: Dr Martin Pellowe, Osteopath (B.Clin.Sci (Ost) M.Ost BSC ECON (Hons)

Colors
0094D4
00A9DD
6FCCEA
C7EBF8
E9F6FB

Requirements
Must have
• logo on the back
Nice to have
• Maybe a space for me to write an appointment time and date on the card.

```html
<!DOCTYPE html>
<html lang="en">
<head>
<meta charset="utf-8">
<title>Brookfarrow Osteopathy and Dry Needling – Business Card</title>
<link href="https://fonts.googleapis.com/css2?family=Montserrat:wght@300;400;600;700&display=swap" rel="stylesheet">
<style>
  :root {
    --bg: #1c1c1e;
    --navy: #0b1a6e;
    --navy-deep: #08155c;
    --blue: #2b86e0;
    --ring: #2f8ae6;
    --sky: #6fcfff;
    --white: #ffffff;
  }
  html, body {
    margin: 0;
    width: 1200px;
    height: 1200px;
    overflow: hidden;
    background: var(--bg);
    font-family: "Montserrat", sans-serif;
  }
  .canvas {
    position: relative;
    width: 1200px;
    height: 1200px;
  }
  .card {
    position: absolute;
    left: 150px;
    width: 900px;
    height: 515px;
    overflow: hidden;
    box-shadow: 0 18px 40px rgba(0,0,0,.45);
  }
  .card--back { top: 60px; background: var(--navy); }
  .card--front { top: 625px; background: var(--white); }

  .card__shapes { position: absolute; inset: 0; }

  .brand-mark {
    position: absolute;
    display: flex;
    align-items: center;
    justify-content: center;
    text-align: center;
    border-radius: 50%;
    color: var(--sky);
    font-weight: 600;
    text-transform: uppercase;
    letter-spacing: 0.06em;
    line-height: 1.35;
    box-sizing: border-box;
  }
  .card--back .brand-mark {
    left: 300px; top: 107px;
    width: 300px; height: 300px;
    border: 4px solid var(--sky);
    font-size: 20px;
    padding: 40px;
  }
  .card--front .brand-mark {
    left: 575px; top: 35px;
    width: 280px; height: 280px;
    font-size: 19px;
    padding: 40px;
  }

  .identity {
    position: absolute;
    left: 60px;
    top: 175px;
  }
  .identity__name {
    margin: 0;
    color: var(--blue);
    font-weight: 700;
    font-size: 32px;
    line-height: 1.2;
  }
  .identity__credentials {
    margin: 10px 0 0;
    color: var(--white);
    font-weight: 300;
    font-size: 25px;
    line-height: 1.3;
  }

  .contact-list {
    position: absolute;
    left: 60px;
    top: 322px;
    margin: 0;
    padding: 0;
    list-style: none;
  }
  .contact-list__item {
    display: flex;
    align-items: center;
    gap: 14px;
    height: 36px;
    margin-bottom: 6px;
    color: var(--white);
    font-weight: 600;
    font-size: 16px;
    letter-spacing: 0.02em;
  }
  .contact-list__icon {
    width: 30px;
    height: 30px;
    flex: none;
  }
</style>
</head>
<body>
<main class="canvas">

  <section class="card card--back" aria-label="Card back">
    <div class="brand-mark">Brookfarrow Osteopathy and Dry Needling</div>
  </section>

  <section class="card card--front" aria-label="Card front">
    <svg class="card__shapes" width="900" height="515" viewBox="0 0 900 515">
      <circle cx="170" cy="560" r="482" fill="none" stroke="var(--ring)" stroke-width="10"/>
      <circle cx="170" cy="560" r="470" fill="var(--navy-deep)"/>
      <circle cx="715" cy="175" r="158" fill="none" stroke="var(--ring)" stroke-width="8"/>
      <circle cx="715" cy="175" r="140" fill="var(--navy)"/>
    </svg>

    <div class="brand-mark">Brookfarrow Osteopathy and Dry Needling</div>

    <div class="identity">
      <h1 class="identity__name">Dr Martin Pellowe</h1>
      <p class="identity__credentials">(B.Clin.Sci (Ost)<br>M.Ost BSC ECON (Hons)</p>
    </div>

    <ul class="contact-list">
      <li class="contact-list__item">
        <svg class="contact-list__icon" viewBox="0 0 32 32"><circle cx="16" cy="16" r="16" fill="var(--blue)"/><rect x="11" y="7" width="10" height="18" rx="2" fill="var(--white)"/><rect x="13" y="9" width="6" height="11" fill="var(--blue)"/></svg>
        www.brookfarrowosteosteopathy.example
      </li>
      <li class="contact-list__item">
        <svg class="contact-list__icon" viewBox="0 0 32 32"><circle cx="16" cy="16" r="16" fill="var(--blue)"/><g fill="none" stroke="var(--white)" stroke-width="1.6"><circle cx="16" cy="16" r="8"/><ellipse cx="16" cy="16" rx="3.5" ry="8"/><line x1="8" y1="16" x2="24" y2="16"/></g></svg>
        www.brookfarrowosteosteopathy.example
      </li>
      <li class="contact-list__item">
        <svg class="contact-list__icon" viewBox="0 0 32 32"><circle cx="16" cy="16" r="16" fill="var(--blue)"/><path d="M16 7a6 6 0 0 0-6 6c0 5 6 12 6 12s6-7 6-12a6 6 0 0 0-6-6z" fill="var(--white)"/><circle cx="16" cy="13" r="2.2" fill="var(--blue)"/></svg>
        48 Lower Crane Street Brookfarrow
      </li>
      <li class="contact-list__item">
        <svg class="contact-list__icon" viewBox="0 0 32 32"><circle cx="16" cy="16" r="16" fill="var(--blue)"/><rect x="8" y="10" width="16" height="12" rx="1.5" fill="var(--white)"/><path d="M8.5 11l7.5 6 7.5-6" fill="none" stroke="var(--blue)" stroke-width="1.6"/></svg>
        www.youremail.example
      </li>
    </ul>
  </section>

</main>
</body>
</html>
```